Logo & Visitenkarte für Hochzeitsplanerin
Zielgruppe
Mein Name ist Leonie Rathke und ich bin Hochzeitsplanerin mit BVR Zertigfikat. Ich komme aus Köln und möchte als selbstständige Hochzeitsplanerin vor allem kölsche Hochzeiten und Hochzeiten mit Marvello Elementen anbieten. Meine Zielgruppe sind junge Brautpaare bis mitte/ende 30 welche genauso heimatverbunden sind wie ich.
Aufgabenstellung
Die Farben rosa und Bordeaux sollen vorkommen und es sollte ein wenig verspielt sein, jedoch nicht zu kindisch. Bitte auf der Visitenkarte noch Hochzeitsplanerin Leonie Rathke (BVR) abbilden.

```html
<!DOCTYPE html>
<html lang="de">
<head>
<meta charset="utf-8">
<title>Herzensband – Visitenkarte</title>
<link rel="stylesheet" href="https://fonts.googleapis.com/css2?family=Overpass:wght@300;400&display=swap">
<style>
  :root {
    --backdrop: #a9243e;
    --card-light: #c73a55;
    --card-mid: #bb2f4a;
    --card-dark: #b02a44;
    --ink: #ffffff;
    --shadow: rgba(70, 8, 22, 0.35);
  }
  * { margin: 0; padding: 0; box-sizing: border-box; }
  html, body {
    width: 1200px;
    height: 900px;
    overflow: hidden;
  }
  body {
    background: var(--backdrop);
    font-family: "Overpass", "Helvetica Neue", Arial, sans-serif;
    color: var(--ink);
    position: relative;
  }
  .card {
    position: absolute;
    top: 305px;
    width: 520px;
    height: 290px;
    background: linear-gradient(135deg, var(--card-dark) 0%, var(--card-light) 55%, var(--card-mid) 100%);
    box-shadow: 0 6px 18px var(--shadow);
  }
  .card--front { left: 50px; }
  .card--back { left: 630px; }

  .brand {
    position: absolute;
    inset: 0;
    display: flex;
    flex-direction: column;
    align-items: center;
    justify-content: center;
    gap: 18px;
  }
  .brand__dot {
    width: 44px;
    height: 44px;
    border: 3px solid var(--ink);
    border-radius: 50%;
  }
  .brand__name {
    font-size: 36px;
    font-weight: 300;
    letter-spacing: 0.02em;
  }

  .card__mark {
    position: absolute;
    top: 30px;
    right: 36px;
    width: 40px;
    height: 40px;
    border: 3px solid var(--ink);
    border-radius: 50%;
  }
  .contact {
    position: absolute;
    left: 31px;
    top: 124px;
    font-size: 11px;
    font-weight: 300;
    line-height: 14.5px;
    font-style: normal;
  }
  .contact p + p { margin-top: 9px; }
</style>
</head>
<body>
  <section class="card card--front" aria-label="Vorderseite der Visitenkarte">
    <div class="brand">
      <span class="brand__dot" aria-hidden="true"></span>
      <span class="brand__name">Herzensband</span>
    </div>
  </section>

  <section class="card card--back" aria-label="Rückseite der Visitenkarte">
    <span class="card__mark" aria-hidden="true"></span>
    <address class="contact">
      <p>Leonie Rathke (BVR)<br>Hochzeitsplanerin<br>Musterstraße 1<br>123456 Musterstadt</p>
      <p>T 01234 5678910<br>F 01234 5678910</p>
      <p>info@herzensband-koeln.de<br>www.herzensband-koeln.de</p>
    </address>
  </section>
</body>
</html>
```